Time for a better IT consulting company?

We are a mobile computer consulting company, taking care of client's issues remotely or at their site. Website of company www.harbor-techmend.com. Business card is an example of marketing so far.
We moved this year but we still service our existing clients. We have expanded our number of technicians available. We would like to use this card for both new business and reaching out to old business.

Target Market(s)

This should target businesses and referrals to businesses from our existing clients as well as a new client outreach for our new location.

Industry/Entity Type

Computer

Requirements
Must have
• This postcard will let clients know we have moved into or we continue to service their area. Make sure it says Inc, not LLC. Must incorporate existing theme in some fashion.
Nice to have
• Themes to communicate: team of people standing by, stability, faster response time, accessibility.
• Areas of coverage: Westchester, Rockland, Manhattan, The Bronx, lower Connecticut.
Should not have
• Cartoon feel.

```html
<!DOCTYPE html>
<html lang="en">
<head>
<meta charset="utf-8">
<title>Harbor Techmend Computer Consulting – Postcard</title>
<link rel="stylesheet" href="https://fonts.googleapis.com/css2?family=PT+Sans:ital,wght@0,400;0,700;1,400&family=Tinos&display=swap">
<style>
  :root{
    --page:#ebebed;
    --charcoal:#444446;
    --charcoal-deep:#37373a;
    --ink:#3f3f42;
    --white:#ffffff;
    --sky:#3c8fb3;
    --sky-soft:#5fa7c8;
    --navy:#0d1d33;
    --ring:#e4e4e6;
    --ring-inner:#e9f2f9;
  }
  *{box-sizing:border-box;margin:0;padding:0}
  html,body{width:895px;height:1200px;overflow:hidden;background:var(--page)}
  body{position:relative;font-family:"PT Sans",sans-serif}
  .card{position:absolute;left:152px;width:590px;height:457px;overflow:hidden;background:var(--white);
        box-shadow:6px 8px 10px rgba(0,0,0,.35)}
  .card--front{top:85px}
  .card--back{top:632px}
  .card svg.shapes{position:absolute;left:0;top:0}
  .abs{position:absolute}

  .brand{position:absolute;left:22px;top:10px;width:200px;color:var(--ink);font-weight:400}
  .brand__dot{width:78px;height:78px;border-radius:50%;background:var(--ink);margin-left:38px}
  .brand__name{font-size:18px;letter-spacing:.5px;margin-top:14px;line-height:1}
  .brand__sub{font-size:7.5px;letter-spacing:2.6px;margin-top:4px;text-transform:uppercase}

  .phone{left:350px;top:88px;font-family:"Tinos",serif;font-size:38px;color:var(--white);white-space:nowrap}
  .callout{left:33px;top:216px;font-family:"Tinos",serif;font-size:16px;color:var(--white)}
  .services-line{font-family:"Tinos",serif;font-size:15px;color:var(--white);white-space:nowrap}
  .services-line::before{content:"";display:inline-block;border-left:4px solid transparent;border-right:4px solid transparent;
        border-bottom:7px solid var(--white);margin-right:10px;vertical-align:1px}
  .contact{right:12px;top:373px;text-align:right;color:var(--white)}
  .contact__title{font-size:19px;font-weight:700;margin-bottom:4px}
  .contact__line{font-family:"Tinos",serif;font-size:10.5px;line-height:17.5px}

  .panel{left:0;top:143px;width:295px;height:314px;background:var(--charcoal);color:var(--white);padding:17px 0 0 22px}
  .panel__title{font-size:18px;font-weight:400;letter-spacing:.5px;margin-bottom:12px}
  .offer-list{list-style:none}
  .offer-list li{font-size:13px;line-height:20.6px}
  .offer-list li::before{content:"";display:inline-block;border-left:3px solid transparent;border-right:3px solid transparent;
        border-bottom:6px solid var(--white);margin-right:4px;vertical-align:1px}
  .panel__note{font-style:italic;font-size:12px;line-height:16px;text-align:center;margin:14px 22px 0 0}
  .web{right:24px;bottom:14px;font-family:"Tinos",serif;font-size:11px;color:var(--ink)}
</style>
</head>
<body>

<section class="card card--front">
  <svg class="shapes" width="590" height="457" viewBox="0 0 590 457">
    <defs>
      <linearGradient id="techGlow" x1="0" y1="0" x2="1" y2="1">
        <stop offset="0" stop-color="#1a2c44"/>
        <stop offset=".55" stop-color="#1d4f78"/>
        <stop offset="1" stop-color="#0d1d33"/>
      </linearGradient>
    </defs>
    <rect width="590" height="143" fill="var(--charcoal)"/>
    <polygon points="0,0 293,0 208,143 0,143" fill="var(--white)"/>
    <rect y="143" width="590" height="314" fill="url(#techGlow)" role="img" aria-label="Technology image: glowing laptop, network icons and world map"/>
    <polygon points="0,143 210,143 185,165 120,320 70,457 0,457" fill="var(--charcoal-deep)"/>
    <circle cx="560" cy="110" r="88" fill="var(--sky-soft)" opacity=".45"/>
    <circle cx="318" cy="112" r="19" fill="none" stroke="var(--white)" stroke-width="3"/>
    <path d="M309 103c2-2 4-2 5 0l2 4c1 1 0 3-1 4l-1 1c1 3 4 6 7 7l1-1c1-1 3-2 4-1l4 2c2 1 2 3 0 5-2 2-5 3-8 2-7-3-12-8-15-15-1-3 0-6 2-8z" fill="var(--white)"/>
    <polygon points="23,207 330,207 340,225 330,243 23,243" fill="#2b2b2e"/>
    <rect x="23" y="207" width="3" height="36" fill="var(--white)"/>
    <g fill="var(--sky)" opacity=".9">
      <polygon points="106,275 455,275 448,294 96,294"/>
      <polygon points="96,297 448,297 441,316 86,316"/>
      <polygon points="86,319 441,319 434,338 76,338"/>
      <polygon points="76,341 434,341 427,360 66,360"/>
      <polygon points="66,363 427,363 420,382 56,382"/>
      <polygon points="56,385 420,385 412,405 46,405"/>
    </g>
  </svg>

  <div class="brand">
    <div class="brand__dot"></div>
    <div class="brand__name">HARBOR TECHMEND</div>
    <div class="brand__sub">Computer Consulting, Inc</div>
  </div>

  <div class="abs phone">914-555-0182</div>
  <div class="abs callout">Need immediate assistance with a computer issue?</div>

  <div class="abs services-line" style="left:158px;top:276px">We offer on-site business &amp; residential</div>
  <div class="abs services-line" style="left:140px;top:298px">service &amp; repair including: emergency</div>
  <div class="abs services-line" style="left:128px;top:320px">services, IT staffing, IP phones,</div>
  <div class="abs services-line" style="left:114px;top:342px">hardware/software, security</div>
  <div class="abs services-line" style="left:106px;top:364px">reviews, and web development</div>
  <div class="abs services-line" style="left:96px;top:386px">for Mac and PC.</div>

  <div class="abs contact">
    <div class="contact__title">Contact Us</div>
    <div class="contact__line">Harbor Techmend Computer Consulting, Inc</div>
    <div class="contact__line">info@harbor-techmend.com</div>
    <div class="contact__line">harbor-techmend.com</div>
  </div>
</section>

<section class="card card--back">
  <svg class="shapes" width="590" height="457" viewBox="0 0 590 457">
    <circle cx="553" cy="128" r="120" fill="var(--ring)"/>
    <circle cx="553" cy="128" r="90" fill="var(--ring-inner)"/>
  </svg>

  <div class="brand">
    <div class="brand__dot"></div>
    <div class="brand__name">HARBOR TECHMEND</div>
    <div class="brand__sub">Computer Consulting, Inc</div>
  </div>

  <div class="abs panel">
    <h2 class="panel__title">Service Offered</h2>
    <ul class="offer-list">
      <li>It staffing</li>
      <li>Pc &amp; MAC</li>
      <li>Home offices</li>
      <li>Websites &amp; wiring</li>
      <li>Wireless &amp; celluler solution</li>
      <li>New Equipment upgrades &amp; Purchases</li>
      <li>Hardware, software &amp; security consulting</li>
      <li>Server &amp; system monitoring &amp; maintanance</li>
    </ul>
    <p class="panel__note">We have moved, and we still service your area:<br>Westchester, Rockland, Manhattan, The Bronx<br>&amp; lower Connecticut. Thank you for your business.</p>
  </div>

  <div class="abs web">harbor-techmend.com</div>
</section>

</body>
</html>
```